Creative pkg design 4 our craft cannabis vaporizer cartridges that stands out above the so-so boxes

We need a package design for our full spectrum terpene rich vaporizer cannabis cartridges that complies with DVRB regulations and conveys a modern, colorful, clean, natural feel to a youngish market. Our cannabis is from the northwest (USA) where we appreciate the clean air, mountains, rivers and healthiness of the area. We stress quality, purity & sustainability. Our marijuana farm is also a trout farm and our logo uses triangles to symbolize the mountains. We are printing on a white box and like this as a foundation. Our logo is usually either silver and black (text silver or black with background opposite) but we are open to playing with the colors & affects etc. We want our package to pop and stand out from the rest. Our market is obviously marijuana users that are over 21, somewhat sophisticated and focused on value and quality from an experienced, trustworthy company. The DVRB requires special placement of some text and some symbols. See layout file. There is a lot of text required but we're hoping for a cool image or graphic concept incorporated behind or dispersed throughout. Our company is Copper Meadow Distillates (CMD)
Updates

We are extending the deadline until next Wednesday. We updated the brief and are looking for something a little more creative and colorful. Not quite so serious and conservative

Target Market(s)

marijuana users over 21, somewhat sophisticated, healthy and focused on value and quality from an experienced, trustworthy company

Industry/Entity Type

Cannabis - marijuana

Font styles to use
Sans Serif

Requirements
Must have
• Must have required text as stated in layout attachment
Should not have
• Cannot be cartoonish

```html
<!DOCTYPE html>
<html lang="en">
<head>
<meta charset="utf-8">
<title>Copper Meadow Distillates – Cartridge Box</title>
<link rel="stylesheet" href="https://fonts.googleapis.com/css2?family=Bebas+Neue&family=Montserrat:wght@400;500;600;700&family=Playfair+Display:ital,wght@1,400&display=swap">
<style>
  :root {
    --backdrop: #e4eeec;
    --box-white: #ffffff;
    --side-white: #f3f3f3;
    --ink: #111111;
    --plum: #6a1fa0;
    --silver: #a3a3a3;
    --alert-red: #e62a2a;
    --lavender: #8f8cf2;
    --indigo: #4f4ae0;
    --violet: #9a6bc8;
    --navy: #161a3a;
    --night: #0f1230;
  }
  * { box-sizing: border-box; margin: 0; padding: 0; }
  html, body { width: 1200px; height: 1084px; overflow: hidden; }
  body { background: var(--backdrop); position: relative; font-family: "Montserrat", sans-serif; }

  .box { position: absolute; left: 200px; top: 80px; width: 810px; height: 930px; display: flex; box-shadow: 0 14px 30px rgba(0,0,0,.12); }

  /* Side panel */
  .side-panel { width: 270px; height: 100%; background: var(--side-white); padding: 40px 30px 0; text-align: center; position: relative; }
  .story-title { display: inline-block; border: 3px solid var(--plum); padding: 10px 14px; font-family: "Montserrat", sans-serif; font-weight: 400; font-size: 26px; letter-spacing: .5px; color: var(--ink); width: 218px; }
  .story-body { margin-top: 20px; font-family: "Playfair Display", serif; font-style: italic; font-size: 18px; line-height: 1.6; color: var(--ink); letter-spacing: -.4px; }
  .story-body p + p { margin-top: 28px; }
  .story-slogan { position: absolute; left: 0; right: 0; bottom: 40px; font-family: "Montserrat", sans-serif; font-weight: 700; font-size: 24px; line-height: 1.3; color: var(--plum); letter-spacing: -.5px; }

  /* Front panel */
  .front-panel { width: 540px; height: 100%; background: var(--box-white); position: relative; overflow: hidden; }
  .product-type { position: absolute; left: 30px; top: 30px; font-family: "Bebas Neue", sans-serif; font-weight: 400; font-size: 30px; line-height: 1.0; color: var(--ink); letter-spacing: .5px; }
  .warning-placeholder { position: absolute; right: 22px; top: 30px; width: 96px; height: 86px; background: var(--alert-red); border-radius: 8px; }

  .brand-seal { position: absolute; left: 50%; top: 175px; transform: translateX(-50%); width: 160px; height: 160px; border: 3px solid var(--silver); border-radius: 50%; display: flex; align-items: center; justify-content: center; }
  .brand-name { font-family: "Montserrat", sans-serif; font-weight: 600; font-size: 12px; letter-spacing: 1.2px; color: var(--silver); text-align: center; line-height: 1.5; }

  .landscape { position: absolute; left: 0; right: 0; top: 340px; bottom: 0;
    background: linear-gradient(170deg, rgba(255,255,255,0) 0%, var(--lavender) 18%, var(--indigo) 38%, var(--violet) 52%, var(--navy) 70%, var(--night) 100%); }

  .extract-note { position: absolute; left: 32px; top: 520px; font-family: "Playfair Display", serif; font-style: italic; font-size: 25px; line-height: 1.35; color: #fff; }
  .strain-name { position: absolute; left: 30px; top: 594px; font-family: "Bebas Neue", sans-serif; font-weight: 400; font-size: 90px; line-height: 1; color: #fff; letter-spacing: .5px; white-space: nowrap; }

  .potency-table { position: absolute; left: 28px; top: 716px; width: 484px; border: 2px solid #fff; color: #fff; font-family: "Montserrat", sans-serif; font-weight: 500; font-size: 22px; padding: 0 10px; }
  .potency-row { display: flex; justify-content: center; align-items: center; gap: 16px; height: 40px; border-bottom: 2px solid #fff; }
  .potency-row:last-child { border-bottom: none; }
  .potency-row.split { padding: 0; gap: 0; }
  .potency-row.split span { flex: 1; text-align: center; height: 100%; display: flex; align-items: center; justify-content: center; }
  .potency-row.split span:first-child { border-right: 2px solid #fff; }

  .net-weight { position: absolute; left: 50%; transform: translateX(-50%); bottom: 8px; background: #000; color: #fff; font-family: "Montserrat", sans-serif; font-size: 20px; padding: 12px 28px; white-space: nowrap; }
</style>
</head>
<body>
  <div class="box">
    <section class="side-panel">
      <h2 class="story-title">OUR STORY</h2>
      <div class="story-body">
        <p>We grow craft cannabis on a spring fed trout farm in the Columbia River Gorge. Our oils are crafted in small premium batches and are always 100% cannabis derived.</p>
        <p>We’re locals with a commitment to nature, purity and sustainability. We are grateful fro our free flowing water, decreasing our load on Oregon’s resources.</p>
        <p>CMD oils are full spectrum with no additives.</p>
      </div>
      <p class="story-slogan">YOU’LL<br>TASTE THE<br>DIFFERENCE!</p>
    </section>

    <section class="front-panel">
      <h1 class="product-type">Cannabis<br>Extract<br>Cartridge</h1>
      <div class="warning-placeholder" role="img" aria-label="Space for the required regulatory warning symbol"></div>

      <div class="brand-seal">
        <span class="brand-name">COPPER MEADOW<br>FARMS</span>
      </div>

      <div class="landscape" role="img" aria-label="Layered purple and indigo mountains with a river winding through the valley"></div>

      <p class="extract-note">Cannabis Derivved<br>Terpenes + Distillate</p>
      <h2 class="strain-name">STRAIN NAME</h2>

      <div class="potency-table">
        <div class="potency-row split"><span>THC 11%</span><span>CBD 22%</span></div>
        <div class="potency-row"><span>Terpenes 33%</span></div>
        <div class="potency-row"><span>Total Cannabinoids:</span><span>44%</span></div>
      </div>

      <div class="net-weight">1g / 0.035 OZ</div>
    </section>
  </div>
</body>
</html>
```